依頼詳細
オープン前のプレオープンで使用するチラシ依頼です。
キャンペーン価格で5日間限定で初回は初見料と施術代で9000円が500円1日限定で10名

こんなお困りの症状はありませんか?

・整体やマッサージに通っているが、肩がこって仕事や日常生活がつらい
・腰痛で電気をあてたり、整骨院に行っても変化がなく諦めている
・頻繁に頭痛に襲われて辛いので、その度に頭痛薬を飲む
・生理前後に痛みが強く、鎮痛薬を飲んでしまう
・精神薬を処方されたが、いつまで飲み続けるのか不安だけどやめられない
・病院で薬をもらったが一向にめまいが改善しない
の項目はなるべく全部入れたいです。

女性に特化した整体院なのでそこがイメージしやすいデザインがありがたいです。
記載項目
店名:自律神経専門 整体院 ゆらぎ→自律神経専門を目立たせて欲しいです。

URL:https://yuragi-karada.example/

地図→詳細を送りますので作成して頂きたいです。

スタッフ写真もしくは女性が施術している写真を入れて欲しいです。

マンションの外装写真を入れるか目印のマルカワ堂がすぐ近く(ビル1つとなり)なので場所イメージがついたほうがいい気がするのでそこの情報はどちらか入れたいです。
電話番号とラインに関しては7月中に取得します。

院内
・予約優先制
・女性セラピスト指名OK
・施術ルーム完全個室
・キッズスペースあり
・ロゴ
を入れたいです。

サイズ
A4
ページ数
両面
希望イメージ
シンプル 複雑
単色 カラフル
暗い 明るい
日常 高級
遊び心 厳粛
未来的 伝統的
女性的 男性的
希望する色
赤系、緑系、茶系
納品ファイル
• 高解像度JPG (.jpg)
• PNG形式 (.png)
補足説明
可能であれば当社でも内容を修正することができれば助かります。
出来る限りインパクトの強いチラシが希望です。

「自律神経専門」整体院の自律神経専門が目立ちたいです。
宜しくお願い致します。

```html
<!DOCTYPE html>
<html lang="ja">
<head>
<meta charset="UTF-8">
<title>自律神経専門整体院 ゆらぎ</title>
<link href="https://fonts.googleapis.com/css2?family=M+PLUS+Rounded+1c:wght@400;500;700;800&display=swap" rel="stylesheet">
<style>
  :root{
    --green:#6aae3a;
    --green-dark:#4f8f27;
    --green-pale:#eaf4df;
    --beige:#f6efe4;
    --text:#4a4a4a;
    --white:#ffffff;
    --photo-skin:#e3cbb8;
    --photo-light:#eeeae6;
  }
  *{margin:0;padding:0;box-sizing:border-box;}
  html,body{width:846px;height:1200px;overflow:hidden;background:var(--white);}
  body{font-family:"M PLUS Rounded 1c",sans-serif;color:var(--text);}
  .flyer{position:relative;width:846px;height:1200px;overflow:hidden;background:var(--white);}

  .brand-mark{position:absolute;left:32px;top:26px;width:170px;text-align:center;}
  .brand-mark .dot{width:120px;height:120px;border-radius:50%;background:var(--green-pale);border:6px solid var(--green);margin:0 auto;}
  .brand-mark .name{margin-top:8px;font-size:30px;font-weight:700;color:var(--green);letter-spacing:4px;}

  .specialty{position:absolute;left:238px;top:22px;display:flex;gap:5px;}
  .specialty span{display:block;width:58px;height:58px;border-radius:10px;background:var(--green);color:var(--white);font-size:38px;font-weight:700;line-height:58px;text-align:center;}
  .clinic-name{position:absolute;left:300px;top:86px;font-size:124px;font-weight:800;color:var(--green);letter-spacing:30px;line-height:1;}

  .hero-photo{position:absolute;left:0;top:216px;width:846px;height:330px;
    background:linear-gradient(110deg,var(--photo-light) 0%,var(--photo-skin) 40%,#d9c3b3 60%,var(--photo-light) 100%);}
  .hero-fade{position:absolute;left:0;top:486px;width:846px;height:60px;background:linear-gradient(to bottom,rgba(255,255,255,0),var(--white));}

  .features{position:absolute;left:590px;top:350px;list-style:none;background:rgba(255,255,255,.82);padding:8px 12px;border-radius:6px;}
  .features li{display:flex;align-items:center;gap:8px;font-size:19px;font-weight:700;color:#333;line-height:26px;}
  .features svg{flex:none;}

  .about{position:absolute;left:40px;top:556px;width:440px;}
  .about h2{font-size:30px;font-weight:700;color:var(--green);padding-bottom:8px;border-bottom:3px solid var(--green);letter-spacing:1px;}
  .about p{margin-top:14px;font-size:15.5px;line-height:1.72;font-weight:500;}

  .room-photo{position:absolute;left:494px;width:312px;border-radius:4px;}
  .room-photo.kids{top:556px;height:188px;background:linear-gradient(135deg,#f1ede6,#d9e6cf 55%,#efe3d3);}
  .room-photo.treatment{top:758px;height:188px;background:linear-gradient(135deg,#f4f1ec,#e6ddd2 60%,#f0ebe4);}

  .footer{position:absolute;left:0;top:966px;width:846px;height:234px;background:var(--green);color:var(--white);}
  .footer .mark{position:absolute;left:40px;top:40px;width:112px;height:112px;border-radius:50%;background:var(--white);}
  .footer .info{position:absolute;left:176px;top:34px;}
  .footer .title{font-size:30px;font-weight:700;letter-spacing:1px;}
  .footer dl{margin-top:10px;font-size:17px;line-height:1.75;font-weight:500;}
  .footer .map{position:absolute;left:580px;top:32px;width:226px;height:160px;background:var(--white);color:var(--green);font-size:26px;font-weight:500;display:flex;align-items:center;justify-content:center;}
</style>
</head>
<body>
<div class="flyer">
  <div class="brand-mark">
    <div class="dot"></div>
    <div class="name">ゆらぎ</div>
  </div>

  <div class="specialty" aria-label="自律神経専門整体院">
    <span>自</span><span>律</span><span>神</span><span>経</span><span>専</span><span>門</span><span>整</span><span>体</span><span>院</span>
  </div>
  <h1 class="clinic-name">ゆらぎ</h1>

  <div class="hero-photo" role="img" aria-label="女性セラピストが横になった女性の首元を施術している写真"></div>
  <div class="hero-fade"></div>

  <ul class="features">
    <li><svg width="18" height="18" viewBox="0 0 18 18"><rect x="1" y="1" width="16" height="16" fill="#fff" stroke="#333" stroke-width="1.6"/><path d="M4 9l4 4 8-10" fill="none" stroke="#6aae3a" stroke-width="2.6"/></svg>予約優先制</li>
    <li><svg width="18" height="18" viewBox="0 0 18 18"><rect x="1" y="1" width="16" height="16" fill="#fff" stroke="#333" stroke-width="1.6"/><path d="M4 9l4 4 8-10" fill="none" stroke="#6aae3a" stroke-width="2.6"/></svg>女性セラピスト指名OK</li>
    <li><svg width="18" height="18" viewBox="0 0 18 18"><rect x="1" y="1" width="16" height="16" fill="#fff" stroke="#333" stroke-width="1.6"/><path d="M4 9l4 4 8-10" fill="none" stroke="#6aae3a" stroke-width="2.6"/></svg>施術ルーム完全個室</li>
    <li><svg width="18" height="18" viewBox="0 0 18 18"><rect x="1" y="1" width="16" height="16" fill="#fff" stroke="#333" stroke-width="1.6"/><path d="M4 9l4 4 8-10" fill="none" stroke="#6aae3a" stroke-width="2.6"/></svg>キッズスペースあり</li>
  </ul>

  <section class="about">
    <h2>自律神経専門整体院って？</h2>
    <p>「自律神経整体」を提供し当社は3年経過しました。<br>当院では、30〜40代の女性女性の予約や問い合わせを多くいただいております。<br>近年「自律神経」の乱れからくる体の不調がメディアにも取り上げられることが多くなり、当院で提供している「自律神経整体」も多くの雑誌に掲載して頂きました。<br>その中で感じたことが、女性特有の悩み（生理痛、冷え性、更年期障害）などと自律神経が関連している状態への理解は女性同士の方が理解し合え、ご安心いただけるということでした。<br>ストレス社会により自律神経の乱れから関連する不調の方々が増えると推測される現代。<br>女性特有の悩みに特化した整体院を開院しました。</p>
  </section>

  <div class="room-photo kids" role="img" aria-label="子どもたちが遊ぶキッズスペースの写真"></div>
  <div class="room-photo treatment" role="img" aria-label="明るい個室の施術ルームの写真"></div>

  <footer class="footer">
    <div class="mark"></div>
    <div class="info">
      <div class="title">自律神経専門整体院 ゆらぎ</div>
      <dl>
        <div>住所：</div>
        <div>電話：</div>
        <div>URL：https://yuragi-karada.example/</div>
      </dl>
    </div>
    <div class="map" role="img" aria-label="整体院周辺の地図">MAP</div>
  </footer>
</div>
</body>
</html>
```